Bramblewick Therapy Services needs upgraded website

Upgrade current website www.bramblewicktherapy.com.au. Need to incorporate new logo (attached). Family friendly and professional feel. Use of colour green. We are based in Melbourne, Australia and work with children aged 0-16 who have additional needs requiring therapy.

Target Market(s)

Parents of children with special needs.

Industry/Entity Type

Work

Colors
000000

Requirements
Must have
• The current content/ pictures are already on the website and can be replicated, just with a fresh look. Additionally need an FAQ section. Must incorporate logo and have consistency on each page. Needs to be accessible on tablets/devices (current website only shows home page on devices, however actual sites has many sub pages (approx. 7). I will need to be able to easily edit the content down the track and potentially add pages.

```html
<!DOCTYPE html>
<html lang="en">
<head>
<meta charset="utf-8">
<title>Bramblewick Therapy Services</title>
<link rel="stylesheet" href="https://fonts.googleapis.com/css2?family=Didact+Gothic&family=Tinos:wght@400&display=swap">
<style>
:root{
  --lime:#46f20b;
  --forest:#0b5a07;
  --footer:#0c5608;
  --footer-text:#2aa12a;
  --stone:#b4b7a5;
  --menu:#b0b2a0;
  --frame:#4f4f4f;
  --btn:#8d8f80;
  --white:#ffffff;
  --ink:#111111;
  --link-green:#4f7a22;
}
*{margin:0;padding:0;box-sizing:border-box}
html,body{width:1158px;height:1200px;overflow:hidden}
body{position:relative;background:var(--stone);font-family:"Didact Gothic",Arial,sans-serif;color:var(--white)}
.band-top{position:absolute;left:0;top:0;width:1158px;height:218px;background:var(--lime)}
.band-dark{position:absolute;left:0;top:218px;width:1158px;height:348px;background:var(--forest)}
.brand{position:absolute;left:72px;top:58px;display:flex;align-items:center;gap:16px}
.brand-name{color:#0d4a08;font-family:"Didact Gothic",Arial,sans-serif;font-size:44px;line-height:46px;letter-spacing:0}
.brand-name small{display:block;font-size:19px;line-height:22px;letter-spacing:5px}
.brand-mark{width:38px;height:38px;background:#0d4a08}
.nav{position:absolute;top:84px;left:0;width:1158px;height:28px}
.nav a{position:absolute;top:0;color:var(--white);text-decoration:none;font-family:Arial,sans-serif;font-weight:bold;font-size:16px;line-height:22px}
.nav a.current{color:#0d3a06}
.nav .sep{position:absolute;top:-2px;width:1px;height:28px;background:#c9ff9f}
.hero{position:absolute;left:66px;top:176px;width:1000px;height:390px;border:4px solid var(--frame);border-bottom:0;background:var(--menu)}
.hero-corner{position:absolute;left:2px;top:2px;width:22px;height:22px;background:linear-gradient(135deg,#e8e8e8 50%,#9a9a9a 50%)}
.side-menu{position:absolute;left:14px;top:40px;list-style:none}
.side-menu li{height:36px;font-family:Tinos,serif;font-size:16px;color:#4a4a40;display:flex;align-items:center;gap:10px}
.side-menu li::before{content:"";width:12px;height:12px;border-radius:50%;border:3px solid #e8e8e0;background:#9c9e8c}
.side-menu li .cap{color:#0b5a07}
.hero-photo{position:absolute;left:240px;top:0;width:756px;height:386px;background:radial-gradient(ellipse at 50% 55%,#f4f4f2,#dcdcd8)}
.heading{position:absolute;font-size:35px;line-height:40px;font-weight:400;color:var(--white);letter-spacing:0}
.divider-v{position:absolute;left:486px;top:590px;height:480px;border-left:2px dotted #8a8c7c}
.divider-h{position:absolute;top:804px;border-top:2px dotted #8a8c7c}
.date{position:absolute;left:104px;top:680px;width:110px;height:26px;background:var(--ink);color:var(--white);font-family:Tinos,serif;font-size:17px;line-height:26px;text-align:center}
.btn{position:absolute;background:var(--btn);color:var(--white);font-family:Arial,sans-serif;font-weight:bold;font-size:16px;line-height:28px;padding-left:10px}
.news-link{position:absolute;left:105px;top:713px;width:330px;font-family:Tinos,serif;font-size:19px;line-height:27px;color:var(--link-green);text-decoration:underline}
.welcome-text{position:absolute;left:536px;top:672px;width:525px;font-family:Tinos,serif;font-size:13px;line-height:17px}
.therapy-list{position:absolute;left:104px;top:906px;list-style:none}
.therapy-list li{height:26.5px;font-size:16px;display:flex;align-items:center;gap:8px}
.therapy-list li::before{content:"";width:5px;height:5px;background:var(--white);transform:rotate(45deg)}
.therapy-list a{color:var(--white)}
.family-photo{position:absolute;left:544px;top:913px;width:219px;height:139px;border:4px solid var(--white);background:linear-gradient(135deg,#6a7a4a,#9a7060 55%,#c8c2b8)}
.expect-text{position:absolute;left:787px;top:923px;width:330px;font-size:16px;line-height:19px}
.footer{position:absolute;left:0;top:1106px;width:1158px;height:94px;background:var(--footer);color:var(--footer-text);font-size:16px}
.footer span{position:absolute;top:42px}
.footer i{position:absolute;width:2px;background:#1a8a1a}
</style>
</head>
<body>
<div class="band-top"></div>
<div class="band-dark"></div>

<header>
  <div class="brand">
    <div class="brand-name">Bramblewick<small>THERAPY SERVICES</small></div>
    <div class="brand-mark"></div>
  </div>
  <nav class="nav">
    <a class="current" href="#" style="left:798px">Home</a>
    <span class="sep" style="left:858px"></span>
    <a href="#" style="left:880px">Contacts</a>
    <span class="sep" style="left:978px"></span>
    <a href="#" style="left:1002px">FAQ's</a>
  </nav>
</header>

<section class="hero">
  <div class="hero-corner"></div>
  <ul class="side-menu">
    <li><span><span class="cap">O</span>ccupational Therapy</span></li>
    <li>Therapy Services</li>
    <li>Group Sessions</li>
    <li>Training Packages</li>
    <li>Meet the Staff</li>
    <li>Fees/ Funding Options</li>
    <li>Parent Resources</li>
    <li>Job Opportunities</li>
    <li>Links</li>
  </ul>
  <div class="hero-photo" role="img" aria-label="Photo of six children in green shirts jumping joyfully against a white studio background"></div>
</section>

<main>
  <h2 class="heading" style="left:100px;top:604px">OUR NEWS</h2>
  <div class="date">18-03-2015</div>
  <div class="btn" style="left:216px;top:680px;width:196px;height:26px;line-height:26px">more news</div>
  <a class="news-link" href="#">Lorem ipsum dolor sit aradipiscing eent vestimlsartes aecena</a>

  <div class="divider-v"></div>
  <div class="divider-h" style="left:96px;width:348px"></div>
  <div class="divider-h" style="left:528px;width:534px"></div>

  <h2 class="heading" style="left:539px;top:604px">WELCOME!</h2>
  <p class="welcome-text">Bramblewick Therapy Service is a specialist Occupational Therapy (O.T) Provider for children (Aged 0-16). Based in Kestrelvale, Victoria, Bramblewick provides comprehensive private therapy services to children with a braod range of Difficulties and disablities. With a special focus on early intervention, Bramblewick strongl believes in gaol based child and family centered therapy.</p>
  <div class="btn" style="left:930px;top:760px;width:120px;height:28px">read more</div>

  <h2 class="heading" style="left:92px;top:842px">TYPES OF THERAPY</h2>
  <ul class="therapy-list">
    <li><a href="#">Fine Motor Coordination</a></li>
    <li><a href="#">Gross Motor Coordination</a></li>
    <li><a href="#">Upper Limb Function</a></li>
  </ul>
  <div class="btn" style="left:104px;top:1021px;width:122px;height:28px">read more</div>

  <h2 class="heading" style="left:539px;top:840px">WHAT TO EXPECT</h2>
  <div class="family-photo" role="img" aria-label="Photo of a smiling mother outdoors holding a baby and a toddler"></div>
  <p class="expect-text">wih a special focus on early intervention based, child and family centered therapy ideally located in the childs natural enviornment</p>
  <div class="btn" style="left:791px;top:1024px;width:122px;height:28px">read more</div>
</main>

<footer class="footer">
  <span style="left:78px">copyright 2015 .&nbsp; All rights reserved</span>
  <i style="left:417px;top:24px;height:52px;width:3px;background:#1fa31f"></i>
  <span style="left:468px">Home Page</span>
  <i style="left:594px;top:28px;height:44px"></i>
  <span style="left:620px">About Us</span>
  <i style="left:730px;top:28px;height:44px"></i>
  <span style="left:773px;top:40px">Services</span>
  <i style="left:862px;top:28px;height:44px"></i>
  <span style="left:895px;top:40px">Fees/Funding</span>
  <i style="left:1006px;top:28px;height:44px"></i>
  <span style="left:1045px;top:40px">Contacts</span>
</footer>
</body>
</html>
```